Natural, organic, vegan-friendly nutritious food supplements

We need packaging design for a new nutritious food supplement to be launched. The products are organic, natural, with no additives, lactose-free, gluten-free, vegan-friendly, etc. The product is a powder that comes in 40g sachets (need sachet design) which are then put into a box (need box design).

More details in the included zip file. Please do not hesitate to contact us for more information if needed.

Target Market(s)

Everyone interested in healthy food.

Requirements
Must have
• Vibrant colours, must be easy to read and easy to recognise on a shelf.
Natural colours.

```html
<!DOCTYPE html>
<html lang="en">
<head>
<meta charset="utf-8">
<title>Merry Cocoa Zing – Box Dieline</title>
<link href="https://fonts.googleapis.com/css2?family=Grand+Hotel&family=Rye&family=Cabin:wght@400;600&display=swap" rel="stylesheet">
<style>
  :root {
    --cocoa: #3d2219;
    --tan: #c59a6d;
    --cut: #e3262a;
    --thumb: #f2d31b;
    --cream: #ffffff;
    --label-brown: #3a2318;
    --label-tan: #b98a5e;
    --art-tone: #d8cfc6;
    --badge-green: #8dc63f;
    --recycle-green: #2aa84a;
  }
  html, body {
    margin: 0;
    padding: 0;
    width: 1200px;
    height: 960px;
    overflow: hidden;
    background: #ffffff;
  }
  .dieline { display: block; width: 1200px; height: 960px; }
  .panel-cocoa { fill: var(--cocoa); }
  .panel-tan { fill: var(--tan); }
  .cut-line { fill: none; stroke: var(--cut); stroke-width: 2; }
  .fold-line { fill: none; stroke: var(--cut); stroke-width: 2; stroke-dasharray: 8 6; }
  .thumb-cut { fill: none; stroke: var(--thumb); stroke-width: 3; stroke-dasharray: 2 6; stroke-linecap: round; }
  .brand-ring { fill: none; stroke: var(--cream); stroke-width: 3; }
  .brand-name { font-family: 'Grand Hotel', cursive; fill: var(--cream); font-size: 40px; }
  .slogan { font-family: 'Grand Hotel', cursive; fill: var(--cream); font-size: 44px; }
  .net-total { font-family: 'Grand Hotel', cursive; fill: var(--cream); font-size: 24px; }
  .label-card { fill: var(--cream); }
  .label-rule { stroke: var(--label-brown); stroke-width: 1; stroke-dasharray: 2 3; }
  .product-line { font-family: 'Rye', serif; fill: var(--label-tan); font-size: 22px; }
  .product-name { font-family: 'Rye', serif; fill: var(--label-brown); font-size: 52px; }
  .flavour { font-family: 'Grand Hotel', cursive; fill: var(--label-tan); font-size: 26px; }
  .net-single { font-family: 'Grand Hotel', cursive; fill: var(--label-tan); font-size: 19px; }
  .claim-badge { fill: none; stroke: var(--cream); stroke-width: 3; }
  .cert-badge { fill: var(--badge-green); }
  .recycle-badge { fill: var(--recycle-green); }
  .company { font-family: 'Cabin', sans-serif; fill: var(--cream); }
  .company-name { font-size: 19px; }
  .company-origin { font-size: 10px; font-weight: 600; letter-spacing: 3px; }
  .company-web { font-size: 12px; font-weight: 600; letter-spacing: 3.5px; }
</style>
</head>
<body>
<svg class="dieline" viewBox="0 0 2150 1720" xmlns="http://www.w3.org/2000/svg">

  <!-- Base colour fields -->
  <g class="colour-fields">
    <path class="panel-cocoa" d="M110,631 H669 V1067 Q669,1092 644,1092 H110 Z"/>
    <path class="panel-cocoa" d="M669,724 H1079 V1092 H694 Q669,1092 669,1067 Z"/>
    <path class="panel-cocoa" d="M1079,631 H1638 V1067 Q1638,1092 1613,1092 H1104 Q1079,1092 1079,1067 Z"/>
    <path class="panel-cocoa" d="M1663,445 H2048 V1092 H1663 Q1638,1092 1638,1067 V470 Q1638,445 1663,445 Z"/>
    <rect class="panel-tan" x="1638" y="53" width="410" height="392"/>
    <rect class="panel-tan" x="110" y="1092" width="1938" height="397"/>
  </g>

  <!-- Cut and fold lines -->
  <g class="cuts">
    <path class="cut-line" d="M110,724 L116,718 L122,631 H647 L669,700 V724"/>
    <path class="cut-line" d="M669,724 H1079"/>
    <path class="cut-line" d="M1079,724 V700 L1101,631 H1626 L1632,718 L1638,724"/>
    <path class="cut-line" d="M1638,724 V165 Q1640,100 1700,72 H1986 Q2046,100 2048,165 V1284"/>
    <path class="cut-line" d="M1638,165 H1690 V175 M1996,175 V165 H2048"/>
    <path class="cut-line" d="M110,724 V1284"/>
    <path class="cut-line" d="M110,1284 L119,1305 V1489 H660 V1305 L669,1284 L678,1305 V1489 H1070 V1305 L1079,1284 L1088,1305 V1489 H1629 V1305 L1638,1284 L1647,1305 V1489 H2039 V1305 L2048,1284"/>
  </g>
  <g class="folds">
    <path class="fold-line" d="M116,724 H669 M1079,724 H2048"/>
    <path class="fold-line" d="M1690,165 H1996"/>
    <path class="fold-line" d="M669,724 V1284 M1079,724 V1284 M1638,724 V1284"/>
    <path class="fold-line" d="M110,1284 H2048"/>
  </g>

  <!-- Front panel -->
  <g class="front-panel">
    <path class="thumb-cut" d="M672,726 C740,730 762,760 762,820 V872 A112,112 0 0 0 986,872 V820 C986,760 1008,730 1076,726"/>
    <g class="brand-mark">
      <circle class="brand-ring" cx="876" cy="877" r="48"/>
      <text class="brand-name" x="876" y="890" text-anchor="middle">Verda</text>
    </g>
    <g class="product-label">
      <rect class="label-card" x="760" y="1023" width="318" height="139"/>
      <line class="label-rule" x1="770" y1="1030" x2="1050" y2="1030"/>
      <line class="label-rule" x1="770" y1="1128" x2="918" y2="1128"/>
      <line class="label-rule" x1="770" y1="1156" x2="1050" y2="1156"/>
      <line class="label-rule" x1="940" y1="1040" x2="940" y2="1150"/>
      <text class="product-line" x="776" y="1058">MERRY COCOA</text>
      <text class="product-name" x="772" y="1116">ZING</text>
      <text class="flavour" x="778" y="1150">Chocolate &amp; Coconut</text>
      <text class="net-single" x="954" y="1148">Net weight: 40g</text>
      <rect x="946" y="1040" width="104" height="86" rx="6" fill="var(--art-tone)" role="img" aria-label="Sketch of coconut halves and cocoa pod"/>
    </g>
    <text class="net-total" x="1062" y="1254" text-anchor="end">Net weight: 600g (15 x 40g)</text>
  </g>

  <!-- Back panel -->
  <g class="back-panel">
    <text class="slogan" x="1358" y="918" text-anchor="middle">Positive side effects of Verda</text>
    <text class="slogan" x="1358" y="958" text-anchor="middle">are entirely intentional</text>
    <g class="claims">
      <circle class="claim-badge" cx="1205" cy="1140" r="22"/>
      <circle class="claim-badge" cx="1258" cy="1140" r="22"/>
      <circle class="claim-badge" cx="1311" cy="1140" r="22"/>
      <circle class="claim-badge" cx="1364" cy="1140" r="22"/>
      <rect class="cert-badge" x="1407" y="1117" width="66" height="45"/>
      <circle class="recycle-badge" cx="1514" cy="1140" r="24"/>
    </g>
    <g class="company">
      <text class="company-name" x="1351" y="1207">Verda Nourish Ltd.</text>
      <text class="company-origin" x="1351" y="1228">PRODUCED IN DENMARK</text>
      <text class="company-web" x="1351" y="1243">WWW.VERDANOURISH.COM</text>
    </g>
  </g>

  <!-- Tuck flap -->
  <g class="tuck-flap" transform="rotate(180 1840 298)">
    <circle class="brand-ring" cx="1840" cy="298" r="56"/>
    <text class="brand-name" x="1840" y="312" text-anchor="middle">Verda</text>
  </g>
</svg>
</body>
</html>
```